Simple Packaging Design For Camera Company

We need packaging designed for our product. Our product is a lens that fits onto smart phones, allowing better quality photos. We would like the design to be simple. Maybe the front cover with just the Tindel logo and the product name (BROAD VIEW MAX) underneath. the box color a light grey and text black. instead of having a picture of our product we were thinking of a outline sketch of it.

Target Market(s)

anyone looking to take better photos, but not wanting a DSLR

Industry/Entity Type

Digital Camera

Font styles to use
Sans Serif

Requirements
Nice to have
• - A sketch outline of the product. not too detailed
• - Light grey background and black text
Should not have
• stock images

```html
<!DOCTYPE html>
<html lang="en">
<head>
<meta charset="utf-8">
<title>Tindel Broad View Max – Packaging Front</title>
<link rel="stylesheet" href="https://fonts.googleapis.com/css2?family=Saira+Extra+Condensed:wght@400&family=Saira:wght@400&display=swap">
<style>
  :root {
    --page: #ffffff;
    --box: #cfcfcf;
    --box-tab: #d3d3d3;
    --hole: #f7f7f7;
    --ink: #1e1e1e;
    --accent: #c47a45;
    --art-light: #dcdcdc;
    --art-dark: #b9b9b9;
  }
  html, body {
    margin: 0;
    padding: 0;
    width: 1191px;
    height: 1200px;
    overflow: hidden;
    background: var(--page);
  }
  .canvas {
    position: relative;
    width: 1191px;
    height: 1200px;
  }
  .package {
    position: absolute;
    left: 0;
    top: 0;
    display: block;
  }
  .brand-name {
    font-family: "Saira Extra Condensed", sans-serif;
    font-weight: 400;
    font-size: 86px;
    fill: var(--ink);
    text-transform: uppercase;
  }
  .product-name {
    font-family: "Saira", sans-serif;
    font-weight: 400;
    font-size: 36px;
    fill: var(--accent);
    text-transform: uppercase;
  }
</style>
</head>
<body>
  <div class="canvas">
    <svg class="package" width="1191" height="1200" viewBox="0 0 1191 1200">
      <defs>
        <radialGradient id="sketch-tone">
          <stop offset="0" stop-color="var(--art-light)"/>
          <stop offset="1" stop-color="var(--art-dark)"/>
        </radialGradient>
      </defs>
      <rect class="hang-tab" x="433" y="225" width="341" height="140" fill="var(--box-tab)"/>
      <g class="hang-hole" fill="var(--hole)">
        <circle cx="598" cy="262" r="20"/>
        <rect x="536" y="261" width="124" height="27" rx="13.5"/>
      </g>
      <polygon class="box-body" points="433,359 778,359 778,975 414,975 414,375" fill="var(--box)"/>
      <text class="brand-name" x="454" y="556" textLength="279" lengthAdjust="spacingAndGlyphs">TINDEL</text>
      <text class="product-name" x="454" y="602" textLength="279" lengthAdjust="spacingAndGlyphs">BROAD VIEW MAX</text>
      <circle class="product-sketch" cx="597" cy="779" r="85" fill="url(#sketch-tone)" role="img" aria-label="Outline sketch of the phone lens attachment"/>
    </svg>
  </div>
</body>
</html>
```